Wordpress Design Project for Bin Hire company

Kestrel Skip Rentals is a Bin Hire company based in the Western Suburbs of Melbourne (Australia) and was established in 1995.
The colours of the Kestrel Skip Rentals logo are Pantone 188C (Burgundy) and 424C (Grey). We would like the site to include these colours throughout the site.

The current Kestrel Skip Rentals site (www.kestrelskiprentals-example.com.au) has been in operation for a number of years and as we have recently commenced a project to update the Logo and Corporate ID, a new Website is also appropriate.

The Kestrel Skip Rentals site only needs to be a simple site and is unlikely to consist of more than 20 pages. The site is primarily used for people to find our contact details, delivery areas and the measurements/size of of the bins we hire to our customers.

Industry/Entity Type

It Company

Requirements
Must have
• A contact page template (which sends an email) which can be used for a main contact page as well as long form response pages to enhance our 'call to action'
A separate enquiry/order form with configurable options will also be required.
A category (products) page will be required which will list all of our bins, a configurable excerpt of the page contents along with a single photo of each bin (a slider may be used also).
We also require the ability for potential customers to look each bin on it's own page as well as a large image, information about each bin and our terms and conditions.
We would also like configurable titles and meta code for each page.
The site will also need the ability to integrate with Tallyworth Metrics.

```html
<!DOCTYPE html>
<html lang="en">
<head>
<meta charset="utf-8">
<title>Kestrel Skip Rentals</title>
<link rel="stylesheet" href="https://fonts.googleapis.com/css2?family=PT+Sans+Narrow:wght@400;700&family=PT+Sans:wght@400;700&family=Kreon:wght@400;600&display=swap">
<style>
:root{
  --burgundy:#8e0a0a;
  --burgundy-deep:#6a0f0f;
  --nav-red:#990000;
  --grey:#8c8c8c;
  --grey-light:#c9c9c9;
  --page:#f8f8f8;
  --hero-bg:#e2e2e2;
  --white:#ffffff;
  --footer:#7b7b7b;
  --footer-link:#7a0000;
}
*{margin:0;padding:0;box-sizing:border-box}
html,body{width:1200px;height:900px;overflow:hidden}
body{position:relative;background:var(--page);font-family:"PT Sans",Arial,sans-serif}

.brand{position:absolute;left:122px;top:0;width:368px;height:170px;background:var(--white);
  display:flex;align-items:center;gap:14px;padding-left:22px}
.brand-mark{width:34px;height:34px;background:var(--burgundy);flex:none}
.brand-name{font-family:"PT Sans Narrow",sans-serif;font-weight:700;font-size:52px;line-height:50px;
  color:var(--burgundy);text-transform:uppercase;letter-spacing:-1px}

.call{position:absolute;left:655px;top:46px;display:flex;align-items:center;gap:6px}
.call-text{font-family:"PT Sans Narrow",sans-serif;font-weight:700;color:#9a9a9a;letter-spacing:-1px;white-space:nowrap}
.call-text .lead{font-size:32px}
.call-text .num{font-size:44px}

.main-nav{position:absolute;left:0;top:173px;width:1200px;height:76px;
  background:linear-gradient(#4a0000 0,#9b0000 12%,#a00000 50%,#950000 86%,#4a0000 100%);
  box-shadow:0 3px 4px rgba(0,0,0,.25)}
.main-nav ul{list-style:none;position:absolute;top:15px;left:134px;display:flex;height:42px}
.main-nav li{font-family:"PT Sans Narrow",sans-serif;font-size:28px;color:var(--grey-light);
  letter-spacing:-1px;line-height:42px;text-align:center;border-right:1px dashed #c9a0a0}
.main-nav li:last-child{border-right:none}

.hero{position:absolute;left:131px;top:256px;width:950px;height:321px;background:var(--hero-bg);border:1px solid #9a9a9a}
.hero-photo{position:absolute;left:6px;top:8px;width:404px;height:304px;
  background:linear-gradient(160deg,#b9cde0 0%,#d8d8d8 40%,#8a8a8a 70%,#6f6a62 100%)}
.hero-copy{position:absolute;left:0;top:0;font-family:"Kreon",serif;font-weight:600;
  text-shadow:2px 3px 3px rgba(0,0,0,.35);line-height:1}
.hero-copy span{position:absolute;white-space:nowrap}
.hero-title{color:var(--burgundy);font-size:64px;left:478px;top:32px}
.hero-line{color:#959595;font-size:58px}

.info{position:absolute;left:132px;top:580px;width:950px;height:268px;
  background:linear-gradient(#a33a3a 0,#7d1616 12%,#6d1212 100%);box-shadow:0 3px 5px rgba(0,0,0,.45)}
.info-heading{position:absolute;font-family:"PT Sans Narrow",sans-serif;font-size:19px;color:#3d0000;
  letter-spacing:-.5px;border-bottom:1px dotted #d8a0a0;padding-bottom:1px;width:163px}
.divider{position:absolute;top:57px;width:1px;height:125px;background:#c9a2a2}

.contact-form label{position:absolute;left:38px;font-size:11px;color:#f0e0e0}
.contact-form .field{position:absolute;left:96px;width:189px;height:21px;background:var(--white);border:1px solid #ccc}
.contact-form .field.message{height:96px}
.btn{position:absolute;top:230px;height:19px;border-radius:10px;background:#dcdcdc;
  font-size:11px;font-weight:700;color:#333;text-align:center;line-height:19px}

.map{position:absolute;left:353px;top:46px;width:237px;height:129px;
  background:linear-gradient(135deg,#d9d3b4 0%,#f0d27a 45%,#cfd5c8 70%,#e4e6de 100%)}
.address{position:absolute;left:356px;top:180px;font-size:11px;color:#f2e6e6;line-height:16px}
.address dt{display:inline-block;width:56px}
.address dd{display:inline}

.payments-text{position:absolute;left:660px;top:66px;width:206px;text-align:center;
  font-size:14px;font-weight:700;color:#e8dcdc;line-height:25px}
.card{position:absolute;top:130px;height:37px;border:2px solid var(--white)}

.site-footer{position:absolute;left:0;top:856px;width:1200px;height:44px;
  background:linear-gradient(#5f5f5f 0,#7e7e7e 20%,#7b7b7b 100%);text-align:center;font-size:10px}
.footer-links{margin-top:10px;color:var(--footer-link);letter-spacing:.3px}
.footer-links span{color:#222}
.copyright{color:#3a0000;margin-top:2px}
</style>
</head>
<body>

<header>
  <div class="brand">
    <span class="brand-mark"></span>
    <span class="brand-name">Kestrel<br>Skip Rentals</span>
  </div>
  <div class="call">
    <svg width="70" height="70" viewBox="0 0 70 70" aria-hidden="true">
      <circle cx="35" cy="35" r="30" fill="none" stroke="#8e0a0a" stroke-width="5"/>
      <path d="M24 18c4-3 8-2 9 1l2 8c1 3-1 4-3 5 1 6 3 10 7 14 2-1 4-2 6 0l5 6c2 2 1 5-2 7-6 3-12 0-17-7-6-8-10-20-7-34z" fill="#8e0a0a"/>
    </svg>
    <p class="call-text"><span class="lead">CALL US NOW : </span><span class="num">0400 123 456</span></p>
  </div>
</header>

<nav class="main-nav">
  <ul>
    <li style="width:130px">HOME</li>
    <li style="width:199px">PRODUCTS</li>
    <li style="width:157px">ENQUIRY</li>
    <li style="width:238px">DELIVERY AREA</li>
    <li style="width:210px">CONTACT US</li>
  </ul>
</nav>

<section class="hero">
  <div class="hero-photo" role="img" aria-label="Photo of a company skip bin truck"></div>
  <h1 class="hero-copy">
    <span class="hero-title">Walk in bins</span>
    <span class="hero-line" style="left:490px;top:100px">for domestic</span>
    <span class="hero-line" style="left:603px;top:158px">and</span>
    <span class="hero-line" style="left:490px;top:218px">commercial use</span>
  </h1>
</section>

<section class="info">
  <div class="contact-form">
    <h2 class="info-heading" style="left:50px;top:11px">Contact Form</h2>
    <label style="top:45px">Name:</label><span class="field" style="top:43px"></span>
    <label style="top:75px">Email:</label><span class="field" style="top:71px"></span>
    <label style="top:105px">Phone:</label><span class="field" style="top:100px"></span>
    <label style="top:135px">Message:</label><span class="field message" style="top:128px"></span>
    <span class="btn" style="left:200px;width:35px">Clear</span>
    <span class="btn" style="left:247px;width:35px">Send</span>
  </div>

  <span class="divider" style="left:318px"></span>

  <h2 class="info-heading" style="left:362px;top:11px">Contact Us</h2>
  <div class="map" role="img" aria-label="Street map showing the depot location"></div>
  <dl class="address">
    <div>12 Harbour Lane, Seabrook Vic 3999</div>
    <div><dt>Phone:</dt><dd>03 9000 1234</dd></div>
    <div><dt>Fax:</dt><dd>03 9000 5678</dd></div>
    <div><dt>Mobile:</dt><dd>0400 123 456</dd></div>
    <div><dt>E-mail:</dt><dd>hello@kestrelskip-example.com.au</dd></div>
  </dl>

  <span class="divider" style="left:630px"></span>

  <h2 class="info-heading" style="left:678px;top:11px">Payments</h2>
  <p class="payments-text">We accept Cash, Cheque,<br>CardOne &amp; PayVista</p>
  <span class="card" style="left:692px;width:60px;background:#2a2a6a"></span>
  <span class="card" style="left:755px;width:58px;background:#1d3f8f"></span>
</section>

<footer class="site-footer">
  <p class="footer-links">HOME <span>|</span> PRODUCTS <span>|</span> ENQUIRY <span>|</span> DELIVERY AREA <span>|</span> CONTACT US</p>
  <p class="copyright">Copyright © Your Company Name</p>
</footer>

</body>
</html>
```